Design mobile friendly review and ranking site

We're working on a corporate website for reviewing and ranking fellow employees. We need the website to look both fun and professional and it needs to be responsive - to it works on mobile and desktop.

Looking for css and HTML for 3 key pages as well as a header and footer for the site. Also would need any supporting graphics as part of the design.

Target Market(s)

Professionals in their 20s, 30s, and 40s.

Industry/Entity Type

Internet

Coding

Coded - Design and coding required

Number of Pages Required

3 page

Font styles to use
Sans Serif

Requirements
Must have
• 3 key pages we need (note included screenshots for each - these are just super rough cuts so you see examples of the content.)
• a) main-intro: A compelling into page with a login/registration form. Should be sleek/modern/enticing. Also we would show the ranking for the top 3 people to tease people re: content.
• b) main-page: Has two sections: One at the top where you would rate someone and one at the bottom where it shows a ranking of people.
• c) profile page: This is where you view a specific person. You see the person's picture, some info about the person, you see their overall rating, you can rate them, and you also see their historical ratings.
Nice to have
• Note we need css and HTML for this. It should feel as sleek and modern. Note also must be responsive design so it works well in mobile and desktop.

```html
<!DOCTYPE html>
<html lang="en">
<head>
<meta charset="utf-8">
<title>TBD Company Name – Rate &amp; Rank</title>
<link rel="stylesheet" href="https://fonts.googleapis.com/css2?family=Open+Sans:wght@400;600;700&family=Roboto:wght@400;500&display=swap">
<style>
  :root {
    --brand: #3c5a9a;
    --brand-dark: #243f7a;
    --page-bg: #f0f1f3;
    --card-bg: #ffffff;
    --card-border: #dedfe3;
    --text: #333333;
    --text-muted: #666666;
    --link: #34559a;
    --green: #5a9a35;
    --star-on: #f39c12;
    --star-off: #555555;
    --rank-1: #f09e00;
    --rank-2: #5b4a8a;
    --rank-3: #c0392b;
    --avatar-teal: #27a594;
    --avatar-orange: #f4a300;
    --avatar-purple: #5a4686;
    --avatar-red: #b8322a;
    --avatar-navy: #26365e;
    --button-light: #e8e8e8;
  }
  * { box-sizing: border-box; margin: 0; padding: 0; }
  html, body { width: 1200px; height: 793px; overflow: hidden; }
  body {
    position: relative;
    background: var(--page-bg);
    font-family: "Open Sans", Arial, sans-serif;
    color: var(--text);
  }

  /* Header */
  .site-header {
    position: absolute; left: 0; top: 0; width: 1200px; height: 45px;
    background: var(--brand); color: #fff;
  }
  .brand-name {
    position: absolute; left: 26px; top: 13px;
    font-size: 15px; font-weight: 700; letter-spacing: .2px;
  }
  .share-cta {
    position: absolute; left: 238px; top: 0; width: 228px; height: 45px;
    background: var(--brand-dark);
    display: flex; align-items: center; gap: 10px; padding-left: 22px;
    font-size: 12px; font-weight: 600;
  }
  .level-meter { position: absolute; left: 796px; top: 12px; width: 177px; }
  .level-track { position: relative; height: 4px; border-radius: 2px; background: #fff; }
  .level-fill { position: absolute; left: 0; top: 0; width: 93px; height: 4px; border-radius: 2px; background: var(--brand-dark); }
  .level-knob {
    position: absolute; left: 87px; top: -4px; width: 12px; height: 12px;
    border-radius: 50%; background: #fff;
  }
  .level-label {
    position: absolute; left: 796px; top: 25px;
    font-size: 11.5px; font-weight: 600;
  }
  .user-nav {
    position: absolute; left: 1000px; top: 8px; height: 30px;
    display: flex; align-items: center; font-size: 12.5px; font-weight: 600;
  }
  .user-avatar { width: 29px; height: 29px; border-radius: 50%; background: var(--avatar-navy); margin-right: 11px; }
  .user-nav .sep { margin: 0 8px; }
  .logout { display: flex; align-items: center; gap: 5px; }

  /* Cards */
  .card {
    position: absolute; background: var(--card-bg);
    border: 1px solid var(--card-border);
  }
  .rate-card { left: 26px; top: 69px; width: 458px; height: 407px; }
  .ranking-card { left: 499px; top: 69px; width: 675px; height: 612px; }

  .avatar { position: absolute; border-radius: 50%; }

  /* Rate panel */
  .rate-card .avatar { left: 28px; top: 30px; width: 66px; height: 66px; background: var(--avatar-teal); }
  .rate-person-name { position: absolute; left: 10px; width: 148px; top: 108px; text-align: center; font-size: 12px; color: var(--text); }
  .view-reviews { position: absolute; left: 10px; width: 148px; top: 126px; text-align: center; font-size: 12px; color: var(--green); }
  .rate-title { position: absolute; left: 126px; top: 37px; font-size: 14.5px; color: var(--text); }
  .criterion { position: absolute; left: 125px; font-size: 12px; color: var(--text-muted); }
  .criterion .stars { display: block; margin-top: 3px; }
  .comment-label { position: absolute; left: 25px; top: 183px; font-size: 11.5px; color: var(--text); }
  .comment-box {
    position: absolute; left: 27px; top: 208px; width: 398px; height: 117px;
    border: 1px solid #d6d6d6; background: #fff;
  }
  .comment-box .caret { position: absolute; left: 12px; top: 9px; width: 1px; height: 17px; background: #333; }
  .comment-box .grip { position: absolute; right: 3px; bottom: 3px; }
  .btn {
    position: absolute; top: 339px; width: 89px; height: 34px;
    display: flex; align-items: center; justify-content: center;
    font-size: 12px;
  }
  .btn-primary { left: 26px; background: var(--brand); color: #fff; }
  .btn-secondary { left: 119px; background: var(--button-light); color: var(--text); }

  /* Stars */
  .stars { font-size: 11px; letter-spacing: 1.5px; line-height: 1; }
  .stars .on { color: var(--star-on); }
  .stars .off { color: var(--star-off); }

  /* Ranking filters */
  .filter {
    position: absolute; top: 15px; height: 34px;
    border: 1px solid #d9d9d9; background: #fff;
    display: flex; align-items: center; padding-left: 13px;
    font-size: 12px; color: var(--text);
  }
  .filter::after {
    content: ""; position: absolute; right: 13px; top: 15px;
    border-left: 3.5px solid transparent; border-right: 3.5px solid transparent;
    border-top: 4px solid #333;
  }
  .filter-sort { left: 19px; width: 97px; }
  .filter-function { left: 144px; width: 230px; }
  .filter-level { left: 425px; width: 232px; }
  .filter-joiner { position: absolute; top: 24px; font-size: 12px; color: var(--text-muted); }

  .divider { position: absolute; left: 19px; width: 637px; height: 1px; background: #e3e3e3; }

  /* Ranking entries */
  .rank-entry { position: absolute; left: 19px; width: 637px; height: 160px; }
  .rank-entry .avatar { left: 0; top: 12px; width: 61px; height: 61px; }
  .rank-badge { position: absolute; left: 78px; top: 5px; font-size: 12.5px; }
  .rank-name { position: absolute; left: 78px; top: 20px; font-family: "Roboto", Arial, sans-serif; font-size: 17px; color: var(--text); }
  .rank-name small { font-family: "Open Sans", Arial, sans-serif; font-size: 11.5px; color: var(--text-muted); margin-left: 7px; }
  .review-count { position: absolute; left: 78px; top: 51px; font-size: 12.5px; color: var(--text-muted); }
  .review-count a { color: var(--link); text-decoration: none; margin-left: 7px; font-size: 12px; }
  .trait { position: absolute; left: 78px; font-size: 12px; color: var(--text); display: flex; align-items: center; gap: 10px; }

  .rank-1 .rank-badge { color: var(--rank-1); }
  .rank-1 .avatar { background: var(--avatar-orange); }
  .rank-2 .rank-badge { color: var(--rank-2); }
  .rank-2 .avatar { background: var(--avatar-purple); }
  .rank-3 .rank-badge { color: var(--rank-3); }
  .rank-3 .avatar { background: var(--avatar-red); }

  /* Footer */
  .site-footer {
    position: absolute; left: 0; top: 745px; width: 1200px; height: 48px;
    background: var(--brand); color: #fff;
    display: flex; align-items: center; justify-content: center;
    font-size: 12.5px;
  }
</style>
</head>
<body>

<header class="site-header">
  <div class="brand-name">TBD COMPANY NAME</div>
  <div class="share-cta">
    <svg width="13" height="13" viewBox="0 0 14 14" aria-hidden="true">
      <g fill="#fff"><circle cx="11" cy="2.6" r="2.3"/><circle cx="3" cy="7" r="2.3"/><circle cx="11" cy="11.4" r="2.3"/></g>
      <path d="M11 2.6 L3 7 L11 11.4" stroke="#fff" stroke-width="1.3" fill="none"/>
    </svg>
    <span>Share this to get more points !</span>
  </div>
  <div class="level-meter">
    <div class="level-track"><div class="level-fill"></div><div class="level-knob"></div></div>
  </div>
  <div class="level-label">Level 3-41 points to level 4</div>
  <nav class="user-nav">
    <div class="user-avatar" role="img" aria-label="Your profile picture"></div>
    <span>Your Profile</span>
    <span class="sep">|</span>
    <span class="logout">
      <svg width="11" height="13" viewBox="0 0 11 13" aria-hidden="true">
        <path d="M2.8 6 V4 a2.7 2.7 0 0 1 5.4 0 V6" stroke="#fff" stroke-width="1.6" fill="none"/>
        <rect x="0.5" y="5.6" width="10" height="7" rx="1" fill="#fff"/>
        <rect x="4.8" y="8" width="1.4" height="2.4" fill="#3c5a9a"/>
      </svg>
      Logout
    </span>
  </nav>
</header>

<section class="card rate-card">
  <div class="avatar" role="img" aria-label="Profile picture of Michael"></div>
  <div class="rate-person-name">Michael</div>
  <div class="view-reviews">view reviews</div>

  <h2 class="rate-title" style="font-weight:400">Anonymously rate this person for a point :</h2>
  <div class="criterion" style="top:64px">smart
    <span class="stars"><span class="on">★★★★</span><span class="off">★</span></span>
  </div>
  <div class="criterion" style="top:100px">Average Personality
    <span class="stars"><span class="on">★★★</span><span class="off">★★</span></span>
  </div>
  <div class="criterion" style="top:136px">Works crazy hard
    <span class="stars"><span class="on">★★★★★</span></span>
  </div>

  <div class="comment-label">( Optional ) Write an anonymous comment about this person :</div>
  <div class="comment-box">
    <span class="caret"></span>
    <svg class="grip" width="7" height="7" viewBox="0 0 7 7" aria-hidden="true">
      <path d="M6 1 L1 6 M6 4 L4 6" stroke="#aaa" stroke-width="1"/>
    </svg>
  </div>
  <div class="btn btn-primary">Skip</div>
  <div class="btn btn-secondary">Save</div>
</section>

<section class="card ranking-card">
  <div class="filter filter-sort">Best</div>
  <span class="filter-joiner" style="left:130px">in</span>
  <div class="filter filter-function">All Functions</div>
  <span class="filter-joiner" style="left:400px">and</span>
  <div class="filter filter-level">All Levels</div>
  <div class="divider" style="top:62px"></div>

  <article class="rank-entry rank-1" style="top:83px">
    <div class="avatar" role="img" aria-label="Profile picture of Jim Johns"></div>
    <div class="rank-badge">#1 Best</div>
    <div class="rank-name">Jim Johns<small>Points 41</small></div>
    <div class="review-count">Number of reviews :<a href="#">View Details</a></div>
    <div class="trait" style="top:75px">Smarts <span class="stars"><span class="on">★★★</span><span class="off">★★</span></span></div>
    <div class="trait" style="top:94px">Easy to work with <span class="stars"><span class="on">★★★</span><span class="off">★★</span></span></div>
    <div class="trait" style="top:114px">Hard worker <span class="stars"><span class="on">★★★</span><span class="off">★★</span></span></div>
  </article>
  <div class="divider" style="top:231px"></div>

  <article class="rank-entry rank-2" style="top:260px">
    <div class="avatar" role="img" aria-label="Profile picture of Michael"></div>
    <div class="rank-badge">#2 Best</div>
    <div class="rank-name">Michael<small>Points 4</small></div>
    <div class="review-count">Number of reviews :<a href="#">View Details</a></div>
    <div class="trait" style="top:75px">Smarts <span class="stars"><span class="on">★★★</span><span class="off">★★</span></span></div>
    <div class="trait" style="top:94px">Easy to work with <span class="stars"><span class="on">★★★</span><span class="off">★★</span></span></div>
    <div class="trait" style="top:114px">Hard worker <span class="stars"><span class="on">★★★</span><span class="off">★★</span></span></div>
  </article>
  <div class="divider" style="top:408px"></div>

  <article class="rank-entry rank-3" style="top:436px">
    <div class="avatar" role="img" aria-label="Profile picture of Leo Marsh III"></div>
    <div class="rank-badge">#3 Best</div>
    <div class="rank-name">Leo Marsh III<small>Points 3.6</small></div>
    <div class="review-count">Number of reviews :<a href="#">View Details</a></div>
    <div class="trait" style="top:75px">Smarts <span class="stars"><span class="on">★★</span><span class="off">★★★</span></span></div>
    <div class="trait" style="top:94px">Easy to work with <span class="stars"><span class="on">★★★</span><span class="off">★★</span></span></div>
    <div class="trait" style="top:114px">Hard worker <span class="stars"><span class="on">★★★</span><span class="off">★★</span></span></div>
  </article>
</section>

<footer class="site-footer">Copyright 2016 | All Right Reserved</footer>

</body>
</html>
```